R.T.Pell Logging Web design

Our website needs a redesign. We want it to appear professional and easy to navigate. We will be adding videos and pictures to the new website. We do not sell any products on our website. It should be designed for informational purposes. Our company performs timber harvesting and forest management services. Attached is our new company logo.

www.rtpelllogging-example.com if you want to see our current website.

Industry/Entity Type

Graphic Design

Coding

Coded - Design and coding required

```html
<!DOCTYPE html>
<html lang="en">
<head>
<meta charset="utf-8">
<title>R.T. Pell Logging Company</title>
<link href="https://fonts.googleapis.com/css2?family=Open+Sans:wght@400;600;700&display=swap" rel="stylesheet">
<style>
  :root{
    --brown-dark:#2b170b;
    --brown-band:#331c0e;
    --brown-rule:#5c2f14;
    --rust:#8a3a15;
    --frame:#7a2b12;
    --green:#92c83e;
    --nav-green:#6f9a1c;
    --light:#e9e7e7;
    --ink:#1c1c1c;
    --muted:#444;
    --white:#ffffff;
    --btn-grey:#4b4b4b;
  }
  *{box-sizing:border-box;margin:0;padding:0}
  html,body{width:1200px;height:2413px;overflow:hidden}
  body{position:relative;font-family:"Open Sans",Arial,sans-serif;background:var(--light);color:var(--ink)}
  .abs{position:absolute}

  /* Hero */
  .hero{left:0;top:0;width:1200px;height:676px;background:linear-gradient(180deg,#5d6a4a 0%,#3e4a2d 45%,#35502a 75%,#2f4a22 100%)}
  .header-bar{left:0;top:60px;width:1200px;height:98px;background:rgba(43,23,11,.82)}
  .brand{left:98px;top:80px;display:flex;align-items:center;gap:14px;color:var(--white);font-weight:700;font-size:34px;letter-spacing:.5px}
  .brand-mark{width:52px;height:52px;background:var(--rust);border-radius:6px}
  .brand small{display:block;font-size:15px;font-weight:400;letter-spacing:3px;margin-top:-4px}
  .main-nav{right:98px;top:60px;height:98px;display:flex}
  .main-nav a{display:flex;align-items:center;padding:0 20px;height:98px;color:var(--white);text-decoration:none;font-size:14px;border-left:1px solid rgba(255,255,255,.15)}
  .main-nav a.active{background:var(--nav-green);border-left:none}
  .hero-copy{left:142px;top:290px;width:410px;text-align:center;color:var(--white)}
  .hero-copy h1{font-size:46px;font-weight:700;margin-bottom:20px}
  .hero-copy p{font-size:20px;line-height:25px;font-weight:600}
  .slide-arrow{top:375px;width:57px;height:56px;background:rgba(235,235,235,.85);display:flex;align-items:center;justify-content:center}
  .dots{left:565px;top:640px;display:flex;gap:6px}
  .dots span{width:19px;height:19px;border-radius:50%;background:var(--white)}
  .dots span.on{background:#c4471a}

  /* Welcome */
  .welcome{left:0;top:676px;width:1200px;height:304px;background:var(--brown-band)}
  .welcome h2{left:98px;top:45px;color:var(--white);font-size:26px;font-weight:600}
  .welcome h3{left:98px;top:80px;color:var(--green);font-size:33px;font-weight:600}
  .call{right:98px;top:45px;text-align:right}
  .call .label{color:var(--white);font-size:26px;font-weight:600;display:flex;align-items:center;gap:6px;justify-content:flex-end}
  .call .phone{color:var(--green);font-size:33px;font-weight:600;margin-top:4px}
  .welcome .rule{left:98px;top:127px;width:1004px;height:3px;background:var(--brown-rule)}
  .welcome p{left:98px;top:140px;width:1004px;color:var(--white);font-size:11.5px;line-height:16px}
  .btn-more{left:98px;top:215px;width:110px;height:37px;background:var(--rust);color:var(--white);font-size:12px;font-weight:600;display:flex;align-items:center;justify-content:center}

  /* Services */
  .section-title{left:98px;top:1030px;font-size:32px;font-weight:600}
  .section-rule{left:98px;top:1072px;width:1004px;height:3px;background:var(--brown-dark)}
  .service-img{top:1102px;width:492px;height:204px;border:3px solid var(--frame)}
  .service{top:1328px;width:492px;text-align:center}
  .service h4{font-size:34px;font-weight:600}
  .service p{font-size:14.5px;line-height:20px;color:var(--muted);padding:0 12px}

  /* Newsletter */
  .newsletter{left:0;top:1483px;width:1200px;height:126px;background:var(--brown-dark)}
  .nl-label{left:188px;top:42px;color:var(--white);font-size:15px;line-height:18px}
  .nl-input{top:42px;width:257px;height:39px;background:var(--white);font-size:11px;color:#666;padding-left:20px;display:flex;align-items:center}
  .nl-btn{left:912px;top:42px;width:124px;height:39px;background:var(--btn-grey);color:var(--white);font-size:13px;font-weight:700;display:flex;align-items:center;justify-content:center}

  /* Gallery */
  .gallery{left:0;top:1609px;width:1200px;height:596px;background:linear-gradient(180deg,#4c6a6e 0%,#3a5230 35%,#34471f 70%,#2c3b1a 100%)}
  .gallery h2{left:0;top:28px;width:1200px;text-align:center;color:var(--white);font-size:31px;font-weight:600}
  .gallery-panel{left:98px;top:91px;width:1004px;height:475px;background:rgba(255,255,255,.18);border:1px solid rgba(255,255,255,.4)}
  .tabs{left:130px;top:132px;display:flex;gap:24px;font-size:17px;color:var(--white);font-weight:600}
  .tabs .on{color:var(--green)}
  .thumb{width:226px;height:146px;border:3px solid var(--white);display:flex;align-items:center;justify-content:center}
  .thumb.active{border-color:var(--green)}
  .dur{position:absolute;right:3px;bottom:3px;background:rgba(0,0,0,.75);color:var(--white);font-size:11px;padding:1px 5px}

  /* Social + footer */
  .social{left:0;top:2235px;width:1200px;display:flex;justify-content:center;gap:34px}
  .social span{width:34px;height:34px;border-radius:50%;background:#2a2a2a}
  .footer-nav{left:0;top:2316px;width:1200px;height:44px;background:var(--brown-dark);display:flex;align-items:center;justify-content:center;color:var(--white);font-size:11.5px}
  .footer-nav span.sep{margin:0 14px}
  .copyright{left:98px;top:2377px;font-size:14px;color:#333}
</style>
</head>
<body>

<section class="hero abs" role="img" aria-label="Photograph of a pine forest with a marked tree trunk in the foreground"></section>
<div class="header-bar abs"></div>
<div class="brand abs"><span class="brand-mark"></span><div>R.T. PELL<small>LOGGING COMPANY</small></div></div>
<nav class="main-nav abs">
  <a class="active">Home</a><a>About Us</a><a>Location</a><a>Services</a><a>Contact Us</a>
</nav>
<div class="hero-copy abs">
  <h1>Timber Harvesting</h1>
  <p>We are always buying timber in southeast Texas. Call for a free estimate. If you have a timber exemption on your property, call us. We can write timber management plans for you.</p>
</div>
<div class="slide-arrow abs" style="left:0"><svg width="18" height="28" viewBox="0 0 18 28"><path d="M15 2 3 14l12 12" fill="none" stroke="#333" stroke-width="2.5"/></svg></div>
<div class="slide-arrow abs" style="right:0"><svg width="18" height="28" viewBox="0 0 18 28"><path d="M3 2l12 12L3 26" fill="none" stroke="#333" stroke-width="2.5"/></svg></div>
<div class="dots abs"><span class="on"></span><span></span><span></span></div>

<section class="welcome abs">
  <h2 class="abs">Welcome To</h2>
  <h3 class="abs">R.T. Pell Logging Company</h3>
  <div class="call abs">
    <div class="label"><svg width="22" height="22" viewBox="0 0 24 24"><path d="M6.6 10.8a15 15 0 0 0 6.6 6.6l2.2-2.2c.3-.3.7-.4 1-.2 1.1.4 2.3.6 3.6.6.6 0 1 .4 1 1V20c0 .6-.4 1-1 1A17 17 0 0 1 3 4c0-.6.4-1 1-1h3.5c.6 0 1 .4 1 1 0 1.3.2 2.5.6 3.6.1.3 0 .7-.2 1z" fill="#fff"/></svg>Call Us:</div>
    <div class="phone">(936) 555-0142</div>
  </div>
  <div class="rule abs"></div>
  <p class="abs">Receive high-quality professional logging and land clearing services, from R.T. Pell Logging Company based in Pine Hollow, TX. Whether your tract is large or small, our team of experts can provide the resources and solutions you need to get the job done right. Our track record for consistency, timely service, and expertise will continue to keep us competitive in the East Texas timber industry. We pay top dollar for your pine and hardwood timber.</p>
  <div class="btn-more abs">Read More</div>
</section>

<h2 class="section-title abs">Services</h2>
<div class="section-rule abs"></div>
<div class="service-img abs" style="left:98px;background:linear-gradient(180deg,#7f9a52,#5f8a3a 60%,#7ea447)" role="img" aria-label="Photograph of a skidder dragging logs through a pine plantation"></div>
<div class="service-img abs" style="left:610px;background:linear-gradient(180deg,#4d6a34,#5d8a3c 60%,#3f5d28)" role="img" aria-label="Photograph of a forester holding a survey tool in the woods"></div>
<div class="service abs" style="left:98px">
  <h4>Timber Harvesting</h4>
  <p>When necessary we also still cut timber the old fashion way, with a chainsaw .</p>
</div>
<div class="service abs" style="left:610px">
  <h4>Forest Management Services</h4>
  <p>My company is set up to take on almost any job. However, we do not provide dangerous tree removal services, such as cutting next to a house.</p>
</div>

<section class="newsletter abs">
  <svg class="abs" style="left:125px;top:45px" width="38" height="36" viewBox="0 0 38 36"><path d="M2 16 36 2 28 34 18 22zM18 22l18-20M18 22v12l5-7" fill="none" stroke="#fff" stroke-width="2" stroke-linejoin="round"/></svg>
  <div class="nl-label abs">Subscribe to<br>our Newsletter</div>
  <div class="nl-input abs" style="left:356px">Enter Your Name</div>
  <div class="nl-input abs" style="left:634px">Enter Your Email Address</div>
  <div class="nl-btn abs">SUBSCRIBE</div>
</section>

<section class="gallery abs" role="img" aria-label="Photograph of a forested mountain valley as section backdrop">
  <h2 class="abs">Gallery &amp; Videos</h2>
  <div class="gallery-panel abs"></div>
  <div class="tabs abs"><span class="on">ALL</span><span>|</span><span>Pictures</span><span>|</span><span>Videos</span></div>

  <div class="thumb active abs" style="left:125px;top:201px;background:linear-gradient(160deg,#6a7a4a,#3d4f2a)" role="img" aria-label="Photograph of workers in safety gear in the forest">
    <svg width="48" height="48" viewBox="0 0 48 48"><circle cx="24" cy="24" r="20" fill="none" stroke="#fff" stroke-width="3" opacity=".8"/><path d="M24 14v20M14 24h20" stroke="#fff" stroke-width="3" opacity=".8"/></svg>
  </div>
  <div class="thumb abs" style="left:367px;top:201px;background:linear-gradient(160deg,#8fb06a,#4d6b38)" role="img" aria-label="Video still of pine seedlings in trays">
    <svg width="40" height="44" viewBox="0 0 40 44"><path d="M4 2l34 20L4 42z" fill="#fff"/></svg><span class="dur">02:53</span>
  </div>
  <div class="thumb abs" style="left:610px;top:201px;background:linear-gradient(180deg,#8fb4d4,#5a7a4a 45%,#3f5a2c)" role="img" aria-label="Photograph of a worker overlooking a forested valley"></div>
  <div class="thumb abs" style="left:851px;top:201px;background:linear-gradient(160deg,#7a8a5a,#4a5a30)" role="img" aria-label="Photograph of two people measuring a tree"></div>

  <div class="thumb abs" style="left:125px;top:382px;background:linear-gradient(160deg,#5a6e3e,#33451f)" role="img" aria-label="Video still of a forester among pines">
    <svg width="40" height="44" viewBox="0 0 40 44"><path d="M4 2l34 20L4 42z" fill="#fff"/></svg><span class="dur">02:53</span>
  </div>
  <div class="thumb abs" style="left:367px;top:382px;background:linear-gradient(160deg,#8a7a58,#5a5236)" role="img" aria-label="Photograph of an excavator installing a culvert"></div>
  <div class="thumb abs" style="left:610px;top:382px;background:linear-gradient(160deg,#7e9a58,#56703a)" role="img" aria-label="Photograph of a worker cutting brush with a chainsaw"></div>
  <div class="thumb abs" style="left:851px;top:382px;background:linear-gradient(160deg,#6e8a4e,#3f5a2a)" role="img" aria-label="Video still of a crew working in a clearing">
    <svg width="40" height="44" viewBox="0 0 40 44"><path d="M4 2l34 20L4 42z" fill="#fff"/></svg><span class="dur">02:53</span>
  </div>
</section>

<div class="social abs" aria-label="Social links"><span></span><span></span><span></span><span></span><span></span></div>

<nav class="footer-nav abs">
  <span>Home</span><span class="sep">|</span><span>About Us</span><span class="sep">|</span><span>Membership</span><span class="sep">|</span><span>Events</span><span class="sep">|</span><span>News</span><span class="sep">|</span><span>Store</span><span class="sep">|</span><span>Sponsors &amp; Friends</span><span class="sep">|</span><span>Contact Us</span>
</nav>
<div class="copyright abs">Copyright @ 2014. All Rights Reserved.</div>

</body>
</html>
```